Report presentation for measurement or inline reports

First page of report. Our inline reporting will come in a maintenance map. We want a modern first page and a real eye-catcher for a new company based in the Netherlands called: RTP Luchtregeling B.V. We are a service company witch measures, balances and give advices at indoor climate HVAC installations. We would like to see designs that use the color blue. We deliver our services to different buildings: Hospitals, atractions, officebuildings, government buildings, swimming pools and schools. Our website: www.rtpl.nl
Updates

Can you all add the new logo please. The companyname is RTP Luchtregeling B.V.. In witch format can i retrieve the design?

Industry/Entity Type

It Company

Colors
0255a3
3176b5
85abd2
cedeed
eaf1f7
ffffff

Requirements
Must have
• Projectname; projectplace; Inline or measure report; date; logo; companyname. it must be easy printable so not to much colours.
• The companyname is: RTP Luchtregeling B.V.. Please add the name. A new logo is updated.
Nice to have
• Maybe some pictures from hvac installations, buildings or measure

```html
<!DOCTYPE html>
<html lang="en">
<head>
<meta charset="utf-8">
<title>Inline Report – RTP Luchtregeling B.V.</title>
<link rel="stylesheet" href="https://fonts.googleapis.com/css2?family=Quicksand:wght@300&family=Didact+Gothic&display=swap">
<style>
  :root {
    --blue-deep: #0255a3;
    --blue: #3176b5;
    --blue-mid: #85abd2;
    --blue-pale: #cedeed;
    --blue-mist: #eaf1f7;
    --white: #ffffff;
    --ink: #2b3a4d;
  }
  html, body {
    margin: 0;
    padding: 0;
    width: 849px;
    height: 1200px;
    overflow: hidden;
    background: var(--white);
  }
  .cover {
    position: relative;
    width: 849px;
    height: 1200px;
    background: var(--white);
  }
  .cover__panel {
    position: absolute;
    left: 35px;
    top: 38px;
    width: 779px;
    height: 1123px;
    background: var(--blue-pale);
  }
  .cover__title {
    position: absolute;
    left: 57px;
    top: 116px;
    margin: 0;
    font-family: "Quicksand", sans-serif;
    font-weight: 300;
    font-size: 82px;
    line-height: 1;
    letter-spacing: -0.5px;
    color: var(--blue);
  }
  .gallery {
    position: absolute;
    left: 0;
    top: 228px;
    width: 636px;
    height: 322px;
  }
  .gallery__photo {
    position: absolute;
  }
  .photo--indoor-unit {
    left: 0; top: 0; width: 325px; height: 182px;
    background: linear-gradient(160deg, #f2f2f0 0%, #d9dadb 55%, #a9acae 100%);
  }
  .photo--rooftop {
    left: 325px; top: 0; width: 311px; height: 182px;
    background: linear-gradient(180deg, #b9cbe0 0%, #d8d6d0 40%, #8a8d90 100%);
  }
  .photo--fan {
    left: 0; top: 182px; width: 208px; height: 140px;
    background: radial-gradient(circle at 45% 45%, #b7c7dc 0%, #3a5b8e 45%, #1b3565 100%);
  }
  .photo--ducts {
    left: 208px; top: 182px; width: 211px; height: 140px;
    background: linear-gradient(90deg, #6f6a63 0%, #e9e9e7 40%, #c9c3ba 100%);
  }
  .photo--garden-unit {
    left: 419px; top: 182px; width: 217px; height: 140px;
    background: linear-gradient(180deg, #c8b9a6 0%, #7c9a4c 50%, #5a3f2c 100%);
  }
  .cover__rule {
    position: absolute;
    left: 0;
    top: 550px;
    width: 785px;
    height: 4px;
    background: var(--blue);
  }
  .brand {
    position: absolute;
    left: 652px;
    top: 510px;
    display: flex;
    align-items: center;
    gap: 6px;
  }
  .brand__mark {
    width: 26px;
    height: 26px;
    background: var(--blue);
  }
  .brand__name {
    font-family: "Didact Gothic", sans-serif;
    font-size: 14px;
    font-weight: 400;
    color: var(--ink);
  }
  .cover__project {
    position: absolute;
    left: 57px;
    top: 610px;
    margin: 0;
    font-family: "Didact Gothic", sans-serif;
    font-weight: 400;
    font-size: 42px;
    line-height: 1;
    color: var(--blue);
  }
  .cover__meta {
    position: absolute;
    left: 57px;
    top: 757px;
    margin: 0;
    font-family: "Didact Gothic", sans-serif;
    font-size: 28px;
    line-height: 1;
    color: var(--blue);
    white-space: nowrap;
  }
</style>
</head>
<body>
  <main class="cover">
    <div class="cover__panel"></div>

    <h1 class="cover__title">Inline Report</h1>

    <section class="gallery">
      <div class="gallery__photo photo--indoor-unit" role="img" aria-label="Wall-mounted indoor air conditioning unit"></div>
      <div class="gallery__photo photo--rooftop" role="img" aria-label="Rooftop HVAC condenser units with large fans"></div>
      <div class="gallery__photo photo--fan" role="img" aria-label="Close-up of a blue condenser fan grille"></div>
      <div class="gallery__photo photo--ducts" role="img" aria-label="White ventilation ducts on a historic building facade"></div>
      <div class="gallery__photo photo--garden-unit" role="img" aria-label="Outdoor air conditioning unit beside a brick wall and garden"></div>
    </section>

    <div class="cover__rule"></div>

    <div class="brand">
      <span class="brand__mark"></span>
      <span class="brand__name">RTP Solutions</span>
    </div>

    <h2 class="cover__project">Testproject in Testplace</h2>

    <p class="cover__meta">Measured by&nbsp; RTP Luchtregeling B.V. on date</p>
  </main>
</body>
</html>
```